Nutritional Supplement Mini Ad

Hello I would like there to be an un-named supplement in the back with a nice background design, very professional look. I have attached an example. If the one I attached could somehow be used, that would be perfect. essentially, I want an un-marked tub (for legal purposes) in the back ground with a professional design. And I want it to say:

Go grab your preworkout right now and look for these money wasting ingredients! Is your preworkout a scam?

Does it have:
- Agmatine?: lack of human evidence for its effects - tested on diabetic rats - found in fermented beer and cabbage

- N-Acetl-L-Tyrosine?: Found in dairy products, meats, fish, eggs, nuts, beans, oats, and wheat. Insufficient evidence for pre
formance boost.

- Folic Acid? Since 1998, it has been added to cold cereals, flour, breads, pasta, bakery items, cookies, and crackers, as required by federal law.
No preformance boost.
- Arginine? - Paired with studies proving no net effects. May be due to poor absorption rate in intestines.

None of these are proven to enhance your workout or results, they're "Label-Fillers". Is your preworkout a scam?. ZorvaTrek.Com -> Articles

So just a very attractive design thats Very eyecatching. I attached a sample one. If that one could someone how be used and just have my phrase in there instead would be perfect!

Supplement

```html
<!DOCTYPE html>
<html lang="en">
<head>
<meta charset="utf-8">
<title>Is your preworkout a scam?</title>
<link href="https://fonts.googleapis.com/css2?family=Arimo:wght@400;700&family=Oswald:wght@500;600;700&display=swap" rel="stylesheet">
<style>
  :root {
    --bg-dark: #141414;
    --bg-mid: #2a2a2a;
    --orange: #f7941d;
    --peach: #fcc98f;
    --white: #ffffff;
    --grey: #9e9794;
    --body-text: #d6d6d6;
    --card-red: #120707;
    --card-dark: #161616;
    --rule: #6b6b6b;
  }
  * { margin: 0; padding: 0; box-sizing: border-box; }
  html, body { width: 1200px; height: 1200px; overflow: hidden; background: var(--bg-dark); }
  .canvas {
    position: relative; width: 1200px; height: 1200px; overflow: hidden;
    background: radial-gradient(ellipse at 50% 40%, var(--bg-mid) 0%, #1d1d1d 55%, var(--bg-dark) 100%);
    font-family: "Arimo", Arial, sans-serif;
  }
  .headline {
    position: absolute; left: 40px; top: 38px;
    font-weight: 700; font-size: 67px; color: var(--white); letter-spacing: -0.5px; white-space: nowrap;
  }
  .subhead {
    position: absolute; left: 40px; top: 138px;
    font-family: "Oswald", sans-serif; font-weight: 600; font-size: 58px; line-height: 68px;
    color: var(--orange); letter-spacing: -0.5px;
  }
  .question {
    position: absolute; left: 38px; top: 334px; font-size: 52px; color: var(--grey); white-space: nowrap;
  }
  .question strong, .closing strong, .band strong { color: var(--white); font-weight: 700; }
  .does-it-have {
    position: absolute; left: 36px; top: 428px;
    font-family: "Oswald", sans-serif; font-weight: 700; font-size: 118px; line-height: 1;
    color: var(--orange); transform: scaleX(0.86); transform-origin: left;
  }
  .tub { position: absolute; left: 852px; top: 138px; width: 246px; height: 416px; }
  .ingredient { position: absolute; top: 586px; width: 267px; }
  .ingredient-name {
    height: 46px; background: var(--peach); padding-left: 14px;
    font-family: "Oswald", sans-serif; font-weight: 500; font-size: 29px; line-height: 46px; color: #1b1b1b;
  }
  .ingredient-notes {
    margin-top: 23px; height: 233px; padding: 14px 10px 0 9px;
    background: linear-gradient(180deg, #1a1a1a, var(--card-dark));
    font-size: 19px; line-height: 32px; color: var(--body-text);
  }
  .ingredient-notes p + p { margin-top: 18px; }
  .ingredient-notes.tight { line-height: 29px; }
  .ingredient-notes.tight p + p { margin-top: 18px; }
  .ingredient:first-of-type .ingredient-notes { background: var(--card-red); }
  .closing { position: absolute; left: 0; width: 1200px; top: 912px; text-align: center; color: var(--grey); }
  .closing .line-one { font-size: 33px; }
  .closing .line-two { font-size: 47px; margin-top: 2px; }
  .source {
    position: absolute; right: 95px; top: 1015px; font-size: 24px; color: #bdbdbd;
  }
  .band {
    position: absolute; left: 0; top: 1066px; width: 1200px; height: 94px;
    background: #060606; border-top: 3px solid var(--rule); border-bottom: 3px solid var(--rule);
    text-align: center; font-size: 62px; line-height: 88px; color: var(--grey);
  }
</style>
</head>
<body>
<main class="canvas">
  <h1 class="headline">Go grab your preworkout right now</h1>
  <h2 class="subhead">and look for these<br>money wasting ingredients</h2>

  <svg class="tub" viewBox="0 0 246 416" role="img" aria-label="Plain unlabelled white supplement tub">
    <defs>
      <linearGradient id="tubBody" x1="0" x2="1">
        <stop offset="0" stop-color="#8f8f92"/>
        <stop offset="0.35" stop-color="#e4e4e6"/>
        <stop offset="0.7" stop-color="#c8c8cb"/>
        <stop offset="1" stop-color="#7d7d80"/>
      </linearGradient>
      <linearGradient id="tubLid" x1="0" x2="1">
        <stop offset="0" stop-color="#b5b5b7"/>
        <stop offset="0.4" stop-color="#f4f4f5"/>
        <stop offset="1" stop-color="#a3a3a6"/>
      </linearGradient>
    </defs>
    <rect x="4" y="78" width="238" height="334" rx="40" fill="url(#tubBody)"/>
    <rect x="22" y="2" width="202" height="82" rx="18" fill="url(#tubLid)"/>
  </svg>

  <p class="question">Is your <strong>preworkout</strong> a <strong>scam?</strong></p>
  <p class="does-it-have">DOES IT HAVE ?</p>

  <section class="ingredient" style="left:38px">
    <h3 class="ingredient-name">Agmatine</h3>
    <div class="ingredient-notes">
      <p>Lack of human evidence for its effects</p>
      <p>tested on diabetic rats</p>
      <p>found in fermented beer and cabbage</p>
    </div>
  </section>
  <section class="ingredient" style="left:323px">
    <h3 class="ingredient-name">N-Acetl-L-Tyrosine</h3>
    <div class="ingredient-notes">
      <p>Found in dairy products, meats, fish, eggs, nuts, beans, oats, and wheat.</p>
      <p>Insufficient evidence for performance boost.</p>
    </div>
  </section>
  <section class="ingredient" style="left:609px">
    <h3 class="ingredient-name">Folic Acid</h3>
    <div class="ingredient-notes tight">
      <p>Since 1998, it has been added to cold cereals, flour, breads, pasta, bakery items, cookies, &amp; crackers, as required by federal law.</p>
      <p>No preformance boost.</p>
    </div>
  </section>
  <section class="ingredient" style="left:895px">
    <h3 class="ingredient-name">Arginine</h3>
    <div class="ingredient-notes">
      <p>Paired with studies prov-ing no net effects.</p>
      <p>May be due to poor ab-sorption rate in intestines</p>
    </div>
  </section>

  <div class="closing">
    <p class="line-one">None of these are proven to enhance your workout or results,</p>
    <p class="line-two">they are <strong>"Label-Fillers"</strong></p>
  </div>
  <p class="source">www.zorvatrek.com → articles</p>

  <footer class="band">Is your <strong>preworkout</strong> a <strong>scam?</strong></footer>
</main>
</body>
</html>
```